Mindfulness School for Children -- Business Cards

We're looking for business cards for our school directors and owners. We're a mindfulness school for children called tumbling willows. Attached are our logos/icons.

```html
<!DOCTYPE html>
<html lang="en">
<head>
<meta charset="utf-8">
<title>Tumbling Willows – Business Cards</title>
<link rel="stylesheet" href="https://fonts.googleapis.com/css2?family=Source+Sans+3:wght@400;700&display=swap">
<style>
  :root {
    --stage: #2b2d30;
    --paper: #f7f8f8;
    --teal: #3aa9bf;
    --teal-deep: #2a7f93;
    --teal-mid: #3b9fb4;
    --teal-light: #7fcfdc;
    --teal-mist: rgba(160, 225, 235, 0.35);
    --teal-shade: rgba(25, 95, 112, 0.35);
    --mint: #a3d6bb;
    --ink: #4a4f53;
    --white: #ffffff;
  }
  * { box-sizing: border-box; margin: 0; padding: 0; }
  html, body {
    width: 1200px; height: 900px; overflow: hidden;
    background: var(--stage);
    font-family: "Source Sans 3", "Source Sans Pro", sans-serif;
  }
  .sheet {
    width: 1200px; height: 900px;
    display: flex; flex-direction: column; align-items: center; justify-content: center;
    gap: 40px;
  }
  .card {
    position: relative;
    width: 700px; height: 400px;
    border-radius: 4px;
    overflow: hidden;
  }
  .card--front { background: var(--paper); }
  .card--back { background: var(--teal-mid); }
  .person { position: absolute; left: 50px; top: 46px; }
  .person__name {
    color: var(--teal); font-weight: 700; font-size: 24px; letter-spacing: 0.5px;
    text-transform: uppercase; line-height: 1.1;
  }
  .person__title { color: var(--ink); font-size: 17px; margin-top: 2px; }
  .person__rule { width: 60px; height: 4px; background: var(--mint); margin-top: 10px; }
  .contact {
    position: absolute; left: 50px; top: 200px;
    color: var(--ink); font-size: 17px; line-height: 1.25;
  }
  .contact__address { margin-bottom: 8px; }
  .contact__row { display: flex; align-items: center; gap: 8px; }
  .contact__row svg { width: 13px; height: 13px; flex: none; }
  .brand {
    position: absolute; right: 50px; bottom: 30px;
    color: var(--teal); font-size: 42px; font-weight: 400; letter-spacing: 0.5px;
  }
  .back__pattern {
    position: absolute; inset: 0;
    background:
      radial-gradient(circle at 70% 40%, var(--teal-mist) 0%, transparent 55%),
      radial-gradient(circle at 15% 90%, var(--teal-shade) 0%, transparent 50%),
      radial-gradient(circle at 95% 95%, var(--teal-mist) 0%, transparent 40%),
      linear-gradient(135deg, var(--teal-deep) 0%, var(--teal-mid) 40%, var(--teal-light) 100%);
  }
  .back__brand {
    position: absolute; left: 90px; top: 110px;
    display: flex; align-items: center; gap: 14px;
    color: var(--white); font-size: 34px; font-weight: 400; letter-spacing: 0.5px;
  }
  .back__dot { width: 20px; height: 20px; border-radius: 50%; background: var(--white); }
</style>
</head>
<body>
<main class="sheet">
  <section class="card card--front">
    <div class="person">
      <h1 class="person__name">Clara Benton</h1>
      <p class="person__title">Managing Director</p>
      <div class="person__rule"></div>
    </div>
    <div class="contact">
      <p class="contact__address">2040 Elm Avenue Fresno<br>CA 93721, United States</p>
      <p class="contact__row">
        <svg viewBox="0 0 16 16" aria-hidden="true"><path fill="var(--teal)" d="M3.5 1.5l2.5 2.8-1.3 1.6c.9 2 2.5 3.6 4.5 4.5l1.6-1.3 2.8 2.5-1.4 2.4C7 13.5 2.5 9 1.1 2.9z"/></svg>
        (+1) 555.018.2390
      </p>
      <p class="contact__row">
        <svg viewBox="0 0 16 16" aria-hidden="true"><rect x="1" y="3" width="14" height="10" fill="var(--teal)"/><path d="M1 3l7 6 7-6" fill="none" stroke="var(--white)" stroke-width="1.4"/></svg>
        info@tumblingwillows.org
      </p>
      <p class="contact__row">
        <svg viewBox="0 0 16 16" aria-hidden="true"><circle cx="8" cy="8" r="7" fill="var(--teal)"/><path d="M1 8h14M8 1c-3 3.5-3 10.5 0 14M8 1c3 3.5 3 10.5 0 14" fill="none" stroke="var(--white)" stroke-width="1"/></svg>
        www.tumblingwillows.org
      </p>
    </div>
    <p class="brand">tumbling willows</p>
  </section>

  <section class="card card--back">
    <div class="back__pattern" role="img" aria-label="Repeating embossed flower pattern in light and deep teal tones covering the whole card"></div>
    <div class="back__brand"><span class="back__dot"></span>tumbling willows</div>
  </section>
</main>
</body>
</html>
```